Ridgecrest Career Institute needs a unique tri-fold brochure design

I need a tri-fold brochure for my vocational school. We provide Nursing Assistant, Home Healthcare Aide & Phlebotomy classes at our centers and 50 programs online. The theme for our brochure and logo is Opening New Doors. I have all the text for the brochure and simples of brochures that I Like. I want the brochure to stand out and represent high quality and success. I also want the brochure to be easy to read. Yes, I'm also open to different ideas and concepts. lol
Updates

The logo and a sample of the text are now available with my brief.

Thanks,

Reg

Thanks to all the designers who took on the project and emailed me directly! If you have not replied to the invite, email me at, rmolvern47@quillpost.net

Thanks again, 
Reg 

Hello All,

Payment for the project is now GUARANTEED! Feel free to email me directly at rmolvern47@quillpost.net or you can post your first draft on my page. Fyi... full content for the brochure is only available upon request.

Thanks,

Reg

Target Market(s)

18-55 years old, but the vast majority are between the age of 24-45

Industry/Entity Type

School

Requirements
Must have
• Pictures of people in scrubs of all ages.
Should not have
• pictures of people in business wear.

```html
<!DOCTYPE html>
<html lang="en">
<head>
<meta charset="utf-8">
<title>Ridgecrest Career Institute – Tri-fold Brochure</title>
<link href="https://fonts.googleapis.com/css2?family=Arimo:ital,wght@0,400;0,700;1,400&family=Roboto+Condensed:wght@700&family=Questrial&display=swap" rel="stylesheet">
<style>
  :root{
    --deep-blue:#1b56a3;
    --mid-blue:#3f7cc4;
    --pale-blue:#d8e6f5;
    --ink-blue:#3a68ad;
    --sky-text:#8fd0f2;
    --title-blue:#3b6cae;
    --tick-blue:#5fb6e6;
    --white:#ffffff;
    --navy:#1c3d78;
  }
  *{margin:0;padding:0;box-sizing:border-box}
  html,body{width:1200px;height:849px;overflow:hidden;background:#fff}
  body{font-family:"Arimo",Arial,sans-serif}
  .brochure{position:relative;width:1200px;height:849px;overflow:hidden;background:var(--deep-blue)}
  .backdrop{position:absolute;inset:0}
  .panel{position:absolute;top:0;height:849px}
  .panel--left{left:0;width:400px}
  .panel--middle{left:400px;width:420px}
  .panel--right{left:800px;width:400px}

  /* left */
  .intro{position:absolute;left:40px;top:30px;width:330px;color:var(--white);font-size:15.5px;line-height:20px;text-align:center}
  .intro p+p{margin-top:12px}
  .why-title{position:absolute;left:0;top:272px;width:400px;text-align:center;color:var(--navy);font-size:20px}
  .reasons{position:absolute;left:46px;top:300px;width:320px;list-style:none}
  .reasons li{position:relative;padding-left:31px;color:var(--white);font-size:13.3px;line-height:19px;margin-bottom:13px}
  .reasons li:first-child{color:#e7eff9}
  .reasons svg{position:absolute;left:0;top:3px;width:19px;height:19px}

  /* middle */
  .brand{position:absolute;left:0;top:30px;width:420px;text-align:center;color:var(--navy);font-weight:700;font-size:17px;line-height:20px}
  .brand .mark{display:block;width:46px;height:46px;border-radius:50%;background:var(--navy);margin:0 auto 10px}
  .contact{position:absolute;left:0;top:136px;width:420px;text-align:center;color:var(--ink-blue);font-size:14.5px;line-height:21px}
  .contact .small{font-size:13.5px}
  .affiliations{position:absolute;left:45px;top:246px;width:323px;height:75px;background:var(--white);border-radius:8px}
  .affiliations h3{text-align:center;color:var(--mid-blue);font-size:15px;margin-top:5px}
  .badge{position:absolute;background:#c9d5e6}
  .badge--one{left:25px;top:18px;width:34px;height:50px;border-radius:50%/40%;background:#d23c3c}
  .badge--two{left:90px;top:36px;width:100px;height:12px;background:#9aa6b8}
  .badge--three{left:210px;top:28px;width:95px;height:26px;background:var(--navy)}
  .q{position:absolute;left:0;width:420px;text-align:center;color:var(--sky-text);font-size:16.5px;line-height:21px}
  .q--centers{top:351px}
  .q--info{top:443px}
  .centers{position:absolute;left:0;top:375px;width:420px;text-align:center;color:var(--white);font-size:14px;line-height:20px}
  .centers small{font-size:11.5px}
  .options-lead{position:absolute;left:0;top:495px;width:420px;text-align:center;color:var(--white);font-size:13.5px}
  .options{position:absolute;left:42px;top:519px;width:320px;list-style:none}
  .options li{position:relative;padding-left:52px;color:var(--white);font-size:13.3px;line-height:18.5px;margin-bottom:9px}
  .options svg{position:absolute;left:18px;top:2px;width:26px;height:26px}
  .license{position:absolute;left:0;top:806px;width:420px;text-align:center;color:#163a6b;font-size:10.5px;line-height:13px}

  /* right */
  .title{position:absolute;left:45px;top:34px;width:340px;color:var(--title-blue);font-family:"Questrial",sans-serif}
  .title .t1{display:block;font-size:56px;line-height:60px}
  .title .t2{position:absolute;left:130px;top:60px;font-family:"Arimo",sans-serif;font-style:italic;font-size:24px;color:var(--tick-blue)}
  .title .t3{position:absolute;left:180px;top:60px;font-size:36px;letter-spacing:6px}
  .photo{position:absolute;left:20px;top:120px;width:380px;height:325px;background:radial-gradient(ellipse at 55% 45%,#c9a98f 0%,#8aa5c6 45%,rgba(120,160,205,0) 75%)}
  .join{position:absolute;left:40px;top:448px;width:330px;text-align:center;font-family:"Roboto Condensed",sans-serif;color:var(--white);font-size:29px;line-height:32px;text-shadow:1px 2px 3px rgba(0,0,0,.5)}
  .benefits{position:absolute;left:20px;top:530px;width:370px;list-style:none;text-align:center;font-family:"Roboto Condensed",sans-serif;color:var(--white);font-size:21px;line-height:25px}
  .benefits li{margin-bottom:9px}
  .benefits li:last-child{color:#cfe3f6}
  .footer-contact{position:absolute;left:60px;top:797px;width:210px;text-align:center;color:var(--ink-blue);font-size:14px;line-height:17px}
  .footer-brand{position:absolute;left:295px;top:775px;width:100px;text-align:center;color:var(--navy);font-weight:700;font-size:11px;line-height:12px}
  .footer-brand .mark{display:block;width:26px;height:26px;border-radius:50%;background:var(--navy);margin:0 auto 4px}
</style>
</head>
<body>
<main class="brochure">
  <svg class="backdrop" width="1200" height="849" viewBox="0 0 1200 849" aria-hidden="true">
    <defs>
      <linearGradient id="sea" x1="0" y1="0" x2="0" y2="1">
        <stop offset="0" stop-color="#a9c5e6"/>
        <stop offset=".35" stop-color="#4d86c8"/>
        <stop offset="1" stop-color="#1b56a3"/>
      </linearGradient>
      <filter id="soft"><feGaussianBlur stdDeviation="22"/></filter>
    </defs>
    <rect width="1200" height="849" fill="url(#sea)"/>
    <g filter="url(#soft)" fill="#ffffff">
      <ellipse cx="620" cy="110" rx="230" ry="110" opacity=".9"/>
      <ellipse cx="1030" cy="120" rx="210" ry="140" opacity=".95"/>
      <path d="M380 460 C520 420 700 500 820 470 L820 520 C700 560 520 490 380 520Z" opacity=".55"/>
      <path d="M420 780 C600 730 760 830 1000 760 L1000 820 C760 880 600 790 420 840Z" opacity=".7"/>
      <ellipse cx="980" cy="790" rx="200" ry="60" opacity=".8"/>
      <path d="M0 250 C120 210 260 280 400 250 L400 290 C260 320 120 260 0 300Z" opacity=".35"/>
    </g>
    <g fill="#1a4f98" opacity=".55">
      <ellipse cx="120" cy="560" rx="200" ry="280"/>
      <ellipse cx="610" cy="650" rx="160" ry="160"/>
    </g>
  </svg>

  <section class="panel panel--left">
    <div class="intro">
      <p>Enroll at the School that completely disregards the status quo, we apply modern innovative methods and techniques to open new doors and help you get the best of both worlds.</p>
      <p>Ridgecrest Career Institute is the door to quickly re-enter the workforce for displaced workers and for individuals looking for fulfilling and rewarding long-term employment while pursuing higher education.</p>
    </div>
    <h2 class="why-title">Why RCI?</h2>
    <ul class="reasons">
      <li><svg viewBox="0 0 19 19"><rect x="1" y="3" width="15" height="15" fill="none" stroke="#5fb6e6" stroke-width="2"/><path d="M4 10l4 4 9-12" fill="none" stroke="#5fb6e6" stroke-width="2.4"/></svg>Our classes are designed with our students, YOU in mind.</li>
      <li><svg viewBox="0 0 19 19"><rect x="1" y="3" width="15" height="15" fill="none" stroke="#5fb6e6" stroke-width="2"/><path d="M4 10l4 4 9-12" fill="none" stroke="#5fb6e6" stroke-width="2.4"/></svg>We DON’T teach you skills only useful in academic settings and yet completely impractical in the workplace. You do NOT need skills you have to UNLEARN in order to do your job!</li>
      <li><svg viewBox="0 0 19 19"><rect x="1" y="3" width="15" height="15" fill="none" stroke="#5fb6e6" stroke-width="2"/><path d="M4 10l4 4 9-12" fill="none" stroke="#5fb6e6" stroke-width="2.4"/></svg>All CNA, HHA &amp; Phlebotomy students are trained by State Certified instructors with practical real world experience. It is mandatory for all RCI instructors to have a combination of State certifications and at least 2 years of real world experience. Our State Certified instructors have been in the trenches so they know what works.</li>
      <li><svg viewBox="0 0 19 19"><rect x="1" y="3" width="15" height="15" fill="none" stroke="#5fb6e6" stroke-width="2"/><path d="M4 10l4 4 9-12" fill="none" stroke="#5fb6e6" stroke-width="2.4"/></svg>The programs are offered in very close and intimate settings where you receive more attention &amp; personalized hands on training. This solid foundation, when combined with the tireless dedication of our devoted &amp; caring office staff, allows you to efficiently cultivate your natural aptitude and develop your desired skill set in your field(s) of choice.</li>
      <li><svg viewBox="0 0 19 19"><rect x="1" y="3" width="15" height="15" fill="none" stroke="#5fb6e6" stroke-width="2"/><path d="M4 10l4 4 9-12" fill="none" stroke="#5fb6e6" stroke-width="2.4"/></svg>You will obtain Skills, knowledge and build the confidence needed to pursue and attain a rewarding career in the healthcare field.</li>
    </ul>
  </section>

  <section class="panel panel--middle">
    <div class="brand"><span class="mark"></span>Ridgecrest Career Institute</div>
    <div class="contact">
      Main number: 239-555-0148<br>
      Toll Free: 877-555-0162<br>
      <span class="small">Email: hello@ridgecrestcareer.org<br>www.ridgecrestcareer.org</span>
    </div>
    <div class="affiliations">
      <h3>Affiliations</h3>
      <span class="badge badge--one"></span>
      <span class="badge badge--two"></span>
      <span class="badge badge--three"></span>
    </div>
    <h3 class="q q--centers">Where are the local centers located?</h3>
    <p class="centers">Harbor Point FL, . Palm Hollow FL,<br><small>Call or visit our website for address and directions</small></p>
    <h3 class="q q--info">How do I acquire information<br>to attend classes at RCI?</h3>
    <p class="options-lead">You have a plethora of options at your disposal:</p>
    <ul class="options">
      <li><svg viewBox="0 0 26 26"><rect x="2" y="12" width="22" height="12" rx="2" fill="#fff"/><path d="M3 11c3-7 17-7 20 0l-5 2-2-3h-6l-2 3z" fill="#fff"/><circle cx="13" cy="18" r="3" fill="#1b56a3"/></svg>Call our main number to schedule a phone or onsite interview with an admission adviser.</li>
      <li><svg viewBox="0 0 26 26"><circle cx="13" cy="13" r="11" fill="none" stroke="#fff" stroke-width="2"/><ellipse cx="13" cy="13" rx="5" ry="11" fill="none" stroke="#fff" stroke-width="1.5"/><path d="M2 13h22M4 7h18M4 19h18" stroke="#fff" stroke-width="1.5"/></svg>Visit our website to submit your request via email.</li>
      <li><svg viewBox="0 0 26 26"><rect x="1" y="1" width="24" height="24" rx="4" fill="#d84040"/><path d="M6 8h14v8h-8l-4 3v-3H6z" fill="#fff"/></svg>Click the Live Chat button on our website to chat with an adviser.</li>
      <li><svg viewBox="0 0 26 26"><rect x="3" y="3" width="20" height="20" rx="4" fill="#fff"/></svg>Submit your request via our social pages</li>
      <li><svg viewBox="0 0 26 26"><circle cx="13" cy="13" r="12" fill="#9ccf45"/><path d="M7 19l10-12 2 2-10 12-3 1z" fill="#fff"/></svg>If you do not have access to a computer or the time to conduct a proper phone interview, you may also text us to request information for registration.</li>
    </ul>
    <p class="license">Licensed by the Department of Education Commission for<br>Independent Education License # 7320</p>
  </section>

  <section class="panel panel--right">
    <h1 class="title"><span class="t1">Opening</span><span class="t2">New</span><span class="t3">Doors</span></h1>
    <div class="photo" role="img" aria-label="Photo of three smiling healthcare workers in scrubs"></div>
    <h2 class="join">Join Us &amp; Open<br>New Doors</h2>
    <ul class="benefits">
      <li>Affordable Education &amp;<br>Quality Education</li>
      <li>Fast Training &amp; Efficient Training</li>
      <li>High Paying Jobs &amp;<br>Rewarding Careers</li>
      <li>State Certified Caregivers &amp;<br>Highly Rated Employers</li>
      <li>Training Facility &amp; Community</li>
    </ul>
    <p class="footer-contact">Toll Free: 877-555-0162<br>www.ridgecrestcareer.org</p>
    <div class="footer-brand"><span class="mark"></span>Ridgecrest Career Institute</div>
  </section>
</main>
</body>
</html>
```